Small environmental consultancy requires basic yet awesome website design by aspiring and cool desig

We are a small environmental consultancy based in Australia, we have set-out a design brief for our website, using a logo we had completed here on Pixel Harbor as well. We hope you can help us with a website!

Website must be wordpress friendly - we have reserved hosting with them already!

Number of Pages Required

4 page

Requirements
Must have
• use supplied logo
• wordpress
• follow provided brief

```html
<!DOCTYPE html>
<html lang="en">
<head>
<meta charset="utf-8">
<title>Greenfield Advisors</title>
<link rel="stylesheet" href="https://fonts.googleapis.com/css2?family=Open+Sans:wght@400;600;700&family=Oswald:wght@400;500&display=swap">
<style>
:root{
  --green:#8dc63f;
  --green-dark:#6fa52a;
  --ink:#333333;
  --muted:#777777;
  --dark:#2e2e2e;
  --darker:#242424;
  --light:#f1f1f1;
  --line:#dddddd;
  --white:#ffffff;
}
*{box-sizing:border-box;margin:0;padding:0}
html,body{width:1200px;height:2800px;overflow:hidden}
body{font-family:"Open Sans",Arial,sans-serif;color:var(--ink);background:var(--white);font-size:12px;line-height:1.5}
.wrap{width:1000px;margin:0 auto;position:relative}

/* header */
.site-header{height:80px;background:var(--white);position:relative}
.brand{position:absolute;left:0;top:10px;display:flex;align-items:center;gap:10px}
.brand-dot{width:48px;height:48px;border-radius:50%;background:var(--green)}
.brand-name{font-weight:700;font-size:18px;color:var(--green-dark);line-height:1.1;width:120px}
.topbar{position:absolute;right:0;top:8px;display:flex;align-items:center;gap:14px;font-size:11px;color:var(--muted)}
.topbar svg{vertical-align:middle;margin-right:5px}
.socials{display:flex;gap:5px}
.socials span{width:18px;height:18px;background:#cfcfcf;display:block}
.main-nav{position:absolute;right:0;top:40px;height:32px;background:var(--green);display:flex;padding-left:30px}
.main-nav a{color:var(--white);text-decoration:none;font-size:11px;font-weight:600;letter-spacing:.5px;padding:0 16px;line-height:32px}
.main-nav a.active{background:var(--green-dark)}

/* hero */
.hero{height:420px;position:relative;background:radial-gradient(ellipse at 35% 45%,#d8ebc3 0%,#a6cf7e 35%,#6e9d4a 70%,#4e7a33 100%)}
.hero-caption{position:absolute;right:100px;top:120px;width:330px;background:rgba(40,40,40,.75);color:var(--white);font-size:20px;line-height:1.35;padding:16px 20px;font-weight:400}

/* intro */
.intro{height:240px;background:var(--dark);color:var(--white);text-align:center;position:relative;padding-top:80px}
.intro p{font-size:22px;line-height:1.5;width:860px;margin:0 auto}
.intro strong{color:var(--green);font-weight:600}
.intro .notch{position:absolute;left:580px;bottom:-20px}

/* section titles */
.section-title{text-align:center;font-family:"Oswald",Arial,sans-serif;font-size:26px;font-weight:500;color:var(--ink);letter-spacing:.5px}
.section-sub{text-align:center;font-size:11px;color:var(--muted);margin-top:2px}
.title-rule{width:40px;height:3px;background:var(--green);margin:8px auto 0}

/* services */
.services{height:460px;padding-top:62px}
.service-grid{display:grid;grid-template-columns:repeat(4,1fr);gap:20px;margin-top:34px}
.service-card{border:1px solid var(--line);height:200px;padding:14px 16px;position:relative}
.service-icon{width:50px;height:50px;border:2px solid var(--green);border-radius:50%;margin:0 auto 8px;display:flex;align-items:center;justify-content:center}
.service-card h3{font-size:13px;font-weight:700;text-align:center;line-height:1.3;margin-bottom:6px}
.service-card ul{list-style:none;font-size:10px;color:var(--muted);line-height:1.55}
.service-card p{font-size:10px;color:var(--muted);line-height:1.55;text-align:center}
.read-more{position:absolute;left:50%;transform:translateX(-50%);bottom:-10px;background:var(--green);color:var(--white);font-size:10px;font-weight:600;padding:3px 14px}
.btn-all{display:block;width:140px;margin:40px auto 0;background:var(--green);color:var(--white);text-align:center;font-size:10px;font-weight:600;letter-spacing:.5px;padding:6px 0}

/* people */
.people{height:360px;background:var(--light);padding-top:40px}
.people-grid{display:grid;grid-template-columns:1fr 1fr;gap:40px;margin-top:30px}
.person{display:flex;gap:18px}
.person-photo{width:130px;height:160px;flex:none;background:linear-gradient(160deg,#b9c7d0,#6f8591)}
.person h3{color:var(--green-dark);font-size:16px;font-weight:600}
.person .role{font-size:10px;color:var(--muted);margin-bottom:6px}
.person .contact{font-size:10px;color:var(--muted);line-height:1.7}
.person .bio{font-size:10px;color:var(--muted);margin-top:8px;line-height:1.6}

/* partners */
.partners{height:200px;background:var(--darker);color:var(--white);position:relative}
.partners .wrap{display:flex;height:200px;align-items:center}
.partner{width:380px;font-size:11px;line-height:1.55}
.partner-badge{margin-top:14px;width:150px;height:46px;background:var(--white)}
.partner.right{margin-left:auto}
.partner.right .partner-badge{width:90px;margin-left:auto}
.partners-hub{position:absolute;left:50%;top:50%;transform:translate(-50%,-50%);text-align:center}
.partners-hub .ring{width:110px;height:110px;border:2px solid var(--green);border-radius:50%;display:flex;align-items:center;justify-content:center;font-family:"Oswald",Arial,sans-serif;font-size:15px;letter-spacing:.5px;color:var(--green)}

/* projects */
.projects{height:380px;padding-top:42px}
.project-strip{display:flex;margin-top:30px;height:220px}
.project-strip div{flex:1}

/* clients */
.clients{height:280px;padding-top:18px}
.client-row{display:flex;justify-content:space-between;margin-top:40px}
.client{width:170px;height:80px;display:flex;align-items:center;justify-content:center;gap:8px;font-size:13px;font-weight:600;color:#8a8a8a}
.client i{width:14px;height:14px;background:#b5b5b5;display:block}

/* footer */
.site-footer{height:300px;background:var(--dark);color:#bdbdbd;padding-top:34px}
.footer-grid{display:grid;grid-template-columns:repeat(4,1fr);gap:30px}
.footer-grid h4{color:var(--white);font-size:12px;font-weight:700;letter-spacing:.5px;margin-bottom:10px}
.footer-grid p{font-size:10px;line-height:1.7}
.footer-socials{display:flex;gap:5px;margin-top:12px}
.footer-socials span{width:18px;height:18px;background:#555;display:block}
.field{height:20px;background:#e8e8e8;margin-bottom:6px}
.field.tall{height:44px}
.btn-small{display:inline-block;background:var(--green);color:var(--white);font-size:10px;font-weight:600;padding:3px 12px}
.newsletter{display:flex;gap:4px;margin-top:8px}
.newsletter .field{flex:1}
.bottom-bar{height:40px;background:var(--darker);color:#9a9a9a;font-size:10px;line-height:40px}
.to-top{position:absolute;right:0;top:10px;width:20px;height:20px;background:var(--green)}
</style>
</head>
<body>

<header class="site-header">
  <div class="wrap" style="height:80px">
    <div class="brand"><span class="brand-dot"></span><span class="brand-name">Greenfield Advisors</span></div>
    <div class="topbar">
      <span><svg width="12" height="9" viewBox="0 0 12 9"><rect x=".5" y=".5" width="11" height="8" fill="none" stroke="#8dc63f"/><path d="M.5 .5 6 5 11.5.5" fill="none" stroke="#8dc63f"/></svg>hello@greenfieldadvisors.example</span>
      <div class="socials"><span></span><span></span><span></span><span></span></div>
    </div>
    <nav class="main-nav">
      <a class="active">HOME</a><a>SERVICES</a><a>PEOPLE</a><a>CLIENTS</a><a>CONTACT</a>
    </nav>
  </div>
</header>

<section class="hero" role="img" aria-label="Close-up photograph of fresh green leaves with water droplets">
  <div class="hero-caption">Greenfield Advisors offer a range of environmental services</div>
</section>

<section class="intro">
  <p><strong>Greenfield Advisors</strong> is Client focussed, offering highly experienced consultants providing effective and innovative environmental solutions.</p>
  <svg class="notch" width="40" height="20" viewBox="0 0 40 20"><path d="M0 0H40L20 20Z" fill="#2e2e2e"/></svg>
</section>

<section class="services">
  <div class="wrap">
    <h2 class="section-title">OUR SERVICES</h2>
    <div class="section-sub">What we are doing</div>
    <div class="title-rule"></div>
    <div class="service-grid">
      <article class="service-card">
        <div class="service-icon"><svg width="22" height="22" viewBox="0 0 22 22"><rect x="3" y="3" width="16" height="16" fill="none" stroke="#8dc63f" stroke-width="2"/><path d="M7 11l3 3 5-6" fill="none" stroke="#8dc63f" stroke-width="2"/></svg></div>
        <h3>Project Management</h3>
        <ul><li>Site planning and scoping</li><li>Tender documents and review</li><li>Contractor supervision</li><li>Reporting to regulators</li><li>Cost and schedule control</li><li>Close out documentation</li></ul>
        <span class="read-more">Read More</span>
      </article>
      <article class="service-card">
        <div class="service-icon"><svg width="22" height="22" viewBox="0 0 22 22"><path d="M2 17h18M5 17l4-8 3 5 2-3 4 6" fill="none" stroke="#8dc63f" stroke-width="2"/></svg></div>
        <h3>Contaminated Land</h3>
        <p>Our team assess soil and groundwater quality at sites across the region and deliver clear, practical plans for safe land reuse and remediation.</p>
        <span class="read-more">Read More</span>
      </article>
      <article class="service-card">
        <div class="service-icon"><svg width="22" height="22" viewBox="0 0 22 22"><path d="M11 2l9 17H2Z" fill="none" stroke="#8dc63f" stroke-width="2"/><path d="M11 8v5M11 15v2" stroke="#8dc63f" stroke-width="2"/></svg></div>
        <h3>Hazardous Materials &amp; Occupational Hygiene</h3>
        <p>Surveys, sampling and air monitoring for workplaces, with advice that keeps your people safe and your site compliant.</p>
        <span class="read-more">Read More</span>
      </article>
      <article class="service-card">
        <div class="service-icon"><svg width="22" height="22" viewBox="0 0 22 22"><circle cx="11" cy="11" r="8" fill="none" stroke="#8dc63f" stroke-width="2"/><path d="M11 3v16M3 11h16" stroke="#8dc63f" stroke-width="2"/></svg></div>
        <h3>Environmental Assessment and Management</h3>
        <p>Impact studies, approvals support and management plans tailored to each project stage.</p>
        <span class="read-more">Read More</span>
      </article>
    </div>
    <a class="btn-all">VIEW ALL SERVICES</a>
  </div>
</section>

<section class="people">
  <div class="wrap">
    <h2 class="section-title">OUR PEOPLE</h2>
    <div class="title-rule"></div>
    <div class="people-grid">
      <article class="person">
        <div class="person-photo" role="img" aria-label="Portrait photograph of Liam Carter"></div>
        <div>
          <h3>Liam Carter</h3>
          <div class="role">Principal Consultant</div>
          <div class="contact">liam@greenfieldadvisors.example<br>+61 400 000 111</div>
          <p class="bio">Liam has more than fifteen years of consulting experience in contaminated land, site assessment and remediation, and leads our project management team with a practical, client first approach.</p>
        </div>
      </article>
      <article class="person">
        <div class="person-photo" role="img" aria-label="Portrait photograph of Noah Ellis"></div>
        <div>
          <h3>Noah Ellis</h3>
          <div class="role">Senior Consultant</div>
          <div class="contact">noah@greenfieldadvisors.example<br>+61 400 000 222</div>
          <p class="bio">Noah has over ten years of experience in hazardous materials and occupational hygiene, helping clients manage risk, meet compliance and protect workers across many industries.</p>
        </div>
      </article>
    </div>
  </div>
</section>

<section class="partners">
  <div class="wrap">
    <div class="partner">
      We are proud to be associated with Coastal Audit Network, auditors in support of all services by our accredited auditor, Liam Carter.
      <div class="partner-badge" role="img" aria-label="Coastal Audit Network partner badge"></div>
    </div>
    <div class="partners-hub"><div class="ring">OUR PARTNERS</div></div>
    <div class="partner right" style="text-align:right">
      We are proud to be associated with Safety Partners Group, in support of hazardous materials services by our licensed assessor, Noah Ellis.
      <div class="partner-badge" role="img" aria-label="Safety Partners Group partner badge"></div>
    </div>
  </div>
</section>

<section class="projects">
  <div class="wrap">
    <h2 class="section-title">OUR PROJECTS</h2>
    <div class="title-rule"></div>
  </div>
  <div class="project-strip">
    <div role="img" aria-label="Project photo of workers in protective suits on a site" style="background:linear-gradient(160deg,#c9c1a8,#7d7462)"></div>
    <div role="img" aria-label="Project photo of soil sampling equipment" style="background:linear-gradient(160deg,#8c8f95,#4e5158)"></div>
    <div role="img" aria-label="Project photo of stored drums at an industrial site" style="background:linear-gradient(160deg,#a48a4e,#5c4a2a)"></div>
    <div role="img" aria-label="Project photo of workers in a laboratory" style="background:linear-gradient(160deg,#b7c0c6,#6f7d86)"></div>
    <div role="img" aria-label="Project photo of a consultant inspecting a building interior" style="background:linear-gradient(160deg,#c96c3a,#6d3a20)"></div>
  </div>
</section>

<section class="clients">
  <div class="wrap">
    <h2 class="section-title">OUR CLIENTS</h2>
    <div class="title-rule"></div>
    <div class="client-row">
      <div class="client"><i></i>Northwind Telecom</div>
      <div class="client">Stonebridge Mining</div>
      <div class="client"><i></i>Harbourline</div>
      <div class="client">Ridgeline Water</div>
      <div class="client"><i></i>Tallwood Group</div>
    </div>
  </div>
</section>

<footer class="site-footer">
  <div class="wrap footer-grid">
    <div>
      <h4>ABOUT US</h4>
      <p>Greenfield Advisors is a small consultancy offering environmental and hygiene services to business and government clients with care and rigour.</p>
    </div>
    <div>
      <h4>CONTACT US</h4>
      <p>PO Box 000, Sample Street<br>Brisbane QLD 4000<br>T: +61 7 0000 0000<br>E: hello@greenfieldadvisors.example</p>
      <div class="footer-socials"><span></span><span></span><span></span><span></span></div>
    </div>
    <div>
      <h4>QUICK CONTACT</h4>
      <div class="field"></div>
      <div class="field"></div>
      <div class="field tall"></div>
      <span class="btn-small">Send</span>
    </div>
    <div>
      <h4>NEWSLETTER</h4>
      <p>Sign up for our latest news.</p>
      <div class="newsletter"><div class="field"></div><span class="btn-small" style="height:20px">Go</span></div>
    </div>
  </div>
</footer>
<div class="bottom-bar">
  <div class="wrap">© Copyright Greenfield Advisors<span class="to-top"></span></div>
</div>

</body>
</html>
```